KRT Design Business Card

I need to develop a business card for my real estate design and investment company. Something clean, classic and professional with a modern vibe.

Industry/Entity Type

Real Estate

Font styles to use
Serif
Sans Serif

```html
<!DOCTYPE html>
<html lang="en">
<head>
<meta charset="UTF-8">
<title>KRT Design Business Card</title>
<link href="https://fonts.googleapis.com/css2?family=Questrial&display=swap" rel="stylesheet">
<style>
  :root {
    --page-bg: #e6e6e4;
    --card-white: #fbfbfb;
    --card-dark: #3a3a3a;
    --band-grey: #c9c9c9;
    --ink-light: #ffffff;
    --ink-soft: #d8d8d8;
    --ink-dark: #2b2b2b;
    --card-shadow: rgba(0, 0, 0, 0.18);
  }
  * { margin: 0; padding: 0; box-sizing: border-box; }
  html, body {
    width: 1200px;
    height: 900px;
    overflow: hidden;
    background: var(--page-bg);
    font-family: "Questrial", "Helvetica Neue", Arial, sans-serif;
  }
  .canvas {
    width: 1200px;
    height: 900px;
    display: flex;
    flex-direction: column;
    align-items: center;
    justify-content: center;
    gap: 60px;
  }
  .card {
    position: relative;
    width: 600px;
    height: 343px;
    border-radius: 30px;
    background: var(--card-white);
    overflow: hidden;
    box-shadow: 0 10px 26px var(--card-shadow);
  }
  .card-swoosh {
    position: absolute;
    inset: 0;
    width: 100%;
    height: 100%;
  }
  .brand-name {
    position: absolute;
    color: var(--ink-dark);
    font-weight: 400;
    letter-spacing: 0.06em;
    white-space: nowrap;
  }
  .card-front .brand-name {
    top: 52px;
    left: 250px;
    font-size: 40px;
  }
  .card-back .brand-name {
    top: 50%;
    left: 50%;
    transform: translate(-50%, -50%);
    font-size: 54px;
  }
  .holder {
    position: absolute;
    left: 42px;
    top: 196px;
    color: var(--ink-light);
  }
  .holder-name {
    font-size: 17px;
    letter-spacing: 0.12em;
    text-transform: uppercase;
  }
  .holder-role {
    margin-top: 4px;
    font-size: 11px;
    letter-spacing: 0.12em;
    text-transform: uppercase;
    color: var(--ink-soft);
  }
  .holder-address {
    margin-top: 16px;
    font-size: 12px;
    line-height: 1.6;
    letter-spacing: 0.06em;
    color: var(--ink-soft);
  }
  .contact-list {
    position: absolute;
    right: 34px;
    top: 222px;
    list-style: none;
    color: var(--ink-light);
    font-size: 12px;
    letter-spacing: 0.06em;
  }
  .contact-item {
    display: flex;
    align-items: center;
    justify-content: flex-end;
    gap: 9px;
    height: 21px;
  }
  .contact-icon {
    width: 12px;
    height: 12px;
    flex: none;
  }
</style>
</head>
<body>
<main class="canvas">

  <section class="card card-front" aria-label="Business card front">
    <svg class="card-swoosh" viewBox="0 0 600 343" preserveAspectRatio="none" aria-hidden="true">
      <path d="M0,150 C170,140 380,190 600,150 L600,343 L0,343 Z" fill="#c9c9c9"/>
      <path d="M0,160 C170,152 380,202 600,168 L600,343 L0,343 Z" fill="#3a3a3a"/>
    </svg>

    <div class="brand-name">KRT Design</div>

    <div class="holder">
      <p class="holder-name">Daniel Hart</p>
      <p class="holder-role">Financial Advisor</p>
      <p class="holder-address">42 Harbour Lane,<br>Leeds UK</p>
    </div>

    <ul class="contact-list">
      <li class="contact-item">012 555 0148
        <svg class="contact-icon" viewBox="0 0 12 12" aria-hidden="true"><path d="M3 1 L5 3.5 L4 5 C4.8 6.6 5.6 7.4 7 8 L8.5 7 L11 9 L9.5 11 C5 10.5 1.5 7 1 2.5 Z" fill="#fff"/></svg>
      </li>
      <li class="contact-item">012 555 0149
        <svg class="contact-icon" viewBox="0 0 12 12" aria-hidden="true"><rect x="3" y="0.8" width="6" height="10.4" rx="1.2" fill="none" stroke="#fff" stroke-width="1.1"/><circle cx="6" cy="9.4" r="0.7" fill="#fff"/></svg>
      </li>
      <li class="contact-item">012 555 0150
        <svg class="contact-icon" viewBox="0 0 12 12" aria-hidden="true"><rect x="1" y="4" width="10" height="7" rx="1" fill="none" stroke="#fff" stroke-width="1.1"/><path d="M3 4 V1.5 H9 V4" fill="none" stroke="#fff" stroke-width="1.1"/></svg>
      </li>
      <li class="contact-item">hello@krtdesign.com
        <svg class="contact-icon" viewBox="0 0 12 12" aria-hidden="true"><rect x="0.8" y="2.5" width="10.4" height="7" rx="0.8" fill="none" stroke="#fff" stroke-width="1.1"/><path d="M1 3 L6 7 L11 3" fill="none" stroke="#fff" stroke-width="1.1"/></svg>
      </li>
      <li class="contact-item">www.krtdesign.com
        <svg class="contact-icon" viewBox="0 0 12 12" aria-hidden="true"><circle cx="6" cy="6" r="5" fill="none" stroke="#fff" stroke-width="1.1"/><ellipse cx="6" cy="6" rx="2.2" ry="5" fill="none" stroke="#fff" stroke-width="1"/><path d="M1 6 H11" stroke="#fff" stroke-width="1"/></svg>
      </li>
    </ul>
  </section>

  <section class="card card-back" aria-label="Business card back">
    <div class="brand-name">KRT Design</div>
  </section>

</main>
</body>
</html>
```